Boutique Soy Candle Company Needs a Label Design

We need a label design for a boutique soy candle company based in Kelby, South Australia.
We sell high quality, hand poured soy wax candles, melts and reed diffusers.
We are based in a coastal town and would like the label to reflect our rustic, beachy, retro but luxurious feel. I've attached the design we've been using and like the idea but want to have something more professional. The picture of the Tandry Column is something that we would like to be included somehow - it's like our town symbol - a 'lighthouse' of sorts. It was quite stylised on my original design but we are open to different interpretations.
We like the idea of a 'Kraft' brown paper sort of label but are not set on it. We also love the fluro pink look.

```html
<!DOCTYPE html>
<html lang="en">
<head>
<meta charset="utf-8">
<title>Lumen Soy Candle Co. – Candle Label</title>
<link href="https://fonts.googleapis.com/css2?family=Montserrat:wght@800&display=swap" rel="stylesheet">
<style>
  :root {
    --stage: #3d3d3d;
    --paper: #ffffff;
    --fluro-pink: #e5007e;
  }
  html, body {
    margin: 0;
    padding: 0;
    width: 1200px;
    height: 1120px;
    overflow: hidden;
    background: var(--stage);
  }
  .canvas {
    position: relative;
    width: 1200px;
    height: 1120px;
  }
  .label {
    position: absolute;
    left: 352px;
    top: 294px;
    width: 496px;
    height: 532px;
    background: var(--paper);
  }
  .label-frame {
    position: absolute;
    left: 0;
    top: 0;
  }
  .brand-mark {
    position: absolute;
    left: 0;
    top: 80px;
    width: 496px;
    text-align: center;
    color: var(--fluro-pink);
    font-family: "Montserrat", sans-serif;
    font-weight: 800;
  }
  .brand-dot {
    width: 96px;
    height: 96px;
    margin: 0 auto 14px;
    border-radius: 50%;
    background: var(--fluro-pink);
  }
  .brand-name {
    margin: 0;
    font-size: 78px;
    line-height: 1;
    letter-spacing: 1px;
  }
  .brand-sub {
    margin: 14px 0 0;
    font-size: 20px;
    line-height: 1.05;
    letter-spacing: 1px;
  }
  .ornament {
    position: absolute;
    left: 215px;
    width: 60px;
    height: 10px;
    background: var(--fluro-pink);
    opacity: 0.8;
    border-radius: 5px;
  }
  .ornament-top { top: 377px; }
  .ornament-bottom { top: 446px; }
  .origin {
    position: absolute;
    left: 0;
    top: 398px;
    width: 496px;
    margin: 0;
    text-align: center;
    color: var(--fluro-pink);
    font-family: "Montserrat", sans-serif;
    font-weight: 800;
    font-size: 16px;
    line-height: 21px;
    letter-spacing: 0.6px;
  }
</style>
</head>
<body>
<div class="canvas">
  <section class="label">
    <svg class="label-frame" width="496" height="532" viewBox="0 0 496 532" aria-hidden="true">
      <g fill="none" stroke="var(--fluro-pink)">
        <rect class="frame-outer" x="16" y="18" width="464" height="495" stroke-width="4"/>
        <rect class="frame-inner" x="29" y="31" width="438" height="470" stroke-width="1.5"/>
      </g>
      <g class="frame-corners" fill="var(--fluro-pink)">
        <path d="M29 31 H55 A26 26 0 0 1 29 57 Z"/>
        <path d="M467 31 H441 A26 26 0 0 0 467 57 Z"/>
        <path d="M29 501 H55 A26 26 0 0 0 29 475 Z"/>
        <path d="M467 501 H441 A26 26 0 0 1 467 475 Z"/>
      </g>
    </svg>

    <div class="brand-mark">
      <div class="brand-dot"></div>
      <p class="brand-name">LUMEN</p>
      <p class="brand-sub">SOY CANDLE CO.</p>
    </div>

    <div class="ornament ornament-top" role="img" aria-label="Small decorative flourish"></div>
    <p class="origin">HAND POURED IN KELBY<br>SOUTH AUSTRALIA</p>
    <div class="ornament ornament-bottom" role="img" aria-label="Small decorative flourish"></div>
  </section>
</div>
</body>
</html>
```